Business Card Design For Financial Company

Create a new design for company's business card. The corporate logo is attached in several formats. Our new website design is also attached and we would like the business cards to reflect this.
Card needs to contain the following info:
Name
Job Title
Legal company name - eg Volmar Capital (Asia) Ltd
Address - eg 612-15 Dorrance Plaza,47 Faverly Street, Hong Kong
Direct tel
Main tel
Fax
Email
Website URL
MS word format preferred. Other formats that can be edited on standard PC also OK.
Please note the the "VOLMAR" logo nameĀ font is "Gill Sans MT" on Windows
Target Market(s)
Instituation Investors
Industry/Entity Type
Business

```html
<!DOCTYPE html>
<html lang="en">
<head>
<meta charset="utf-8">
<title>Volmar Capital – Business Card Concepts</title>
<link rel="stylesheet" href="https://fonts.googleapis.com/css2?family=Questrial&display=swap">
<style>
  :root {
    --backdrop: #262626;
    --card: #e6e6e6;
    --ink: #2b2b2b;
    --ink-soft: #555555;
    --ink-muted: #8a8a8a;
    --rule: #3a3a3a;
    --brand-red: #d8343a;
    --brand-red-faint: rgba(216, 52, 58, 0.18);
  }
  * { margin: 0; padding: 0; box-sizing: border-box; }
  html, body {
    width: 1200px; height: 1069px; overflow: hidden;
    background: var(--backdrop);
    font-family: "Questrial", "Century Gothic", sans-serif;
    color: var(--ink);
  }
  .sheet { position: relative; width: 1200px; height: 1069px; }

  .card {
    position: absolute;
    width: 474px; height: 271px;
    background: var(--card);
    border-radius: 10px 30px 30px 10px;
    overflow: hidden;
  }
  .card--front-a { left: 80px;  top: 184px; }
  .card--back-a  { left: 641px; top: 181px; }
  .card--front-b { left: 80px;  top: 630px; }
  .card--back-b  { left: 641px; top: 628px; }

  .brand-dot {
    position: absolute; border-radius: 50%;
    background: var(--brand-red);
  }
  .card--front-a .brand-dot,
  .card--front-b .brand-dot { width: 108px; height: 108px; left: 188px; top: 38px; }

  .wordmark {
    position: absolute; left: 0; width: 100%; top: 160px;
    text-align: center; font-size: 51px; line-height: 1;
    color: var(--ink); letter-spacing: 1px;
  }

  .person {
    position: absolute; left: 27px; top: 53px;
    display: inline-block;
  }
  .person__name { font-size: 30px; line-height: 1; color: var(--ink); white-space: nowrap; }
  .person__title {
    font-size: 10.5px; color: var(--ink-muted);
    text-align: right; margin-top: 2px;
  }
  .company {
    position: absolute; left: 72px; top: 104px;
    font-size: 11px; color: var(--ink-soft); white-space: nowrap;
  }

  .address, .contact {
    position: absolute; color: var(--ink-soft); white-space: nowrap;
  }
  .address { font-size: 9.5px; line-height: 12.5px; }
  .contact { font-size: 10px; line-height: 13px; }

  .divider { position: absolute; width: 2px; background: var(--rule); }

  /* Variant A: faint brand circle at right edge */
  .card--back-a .brand-dot--faint {
    background: var(--brand-red-faint);
    width: 142px; height: 142px; left: 331px; top: 77px;
  }
  .card--back-a .address { left: 35px; top: 195px; }
  .card--back-a .divider { left: 210px; top: 174px; height: 81px; }
  .card--back-a .contact { left: 220px; top: 174px; }

  /* Variant B: solid brand circle at lower left */
  .card--back-b .brand-dot { width: 108px; height: 108px; left: 69px; top: 143px; }
  .card--back-b .divider { left: 232px; top: 148px; height: 107px; }
  .card--back-b .address { left: 258px; top: 147px; }
  .card--back-b .contact { left: 258px; top: 178px; line-height: 14.5px; font-size: 10.5px; }
</style>
</head>
<body>
<main class="sheet">

  <section class="card card--front-a">
    <div class="brand-dot"></div>
    <div class="wordmark">VOLMAR</div>
  </section>

  <section class="card card--back-a">
    <div class="brand-dot brand-dot--faint"></div>
    <div class="person">
      <div class="person__name">Daniel Harrow</div>
      <div class="person__title">Managing Director</div>
    </div>
    <div class="company">Volmar Capital (Asia) Ltd</div>
    <div class="address">Address: 612-15 Dorrance Plaza<br>47 Faverly Street, Hong Kong</div>
    <div class="divider"></div>
    <div class="contact">
      Direct Tel # 0412 557 208<br>
      Main Tel # 0412 557 208<br>
      Fax # 0412 557 208<br>
      Email ID: info@volmar.com<br>
      Website: www.volmar.com
    </div>
  </section>

  <section class="card card--front-b">
    <div class="brand-dot"></div>
    <div class="wordmark">VOLMAR</div>
  </section>

  <section class="card card--back-b">
    <div class="person">
      <div class="person__name">Daniel Harrow</div>
      <div class="person__title">Managing Director</div>
    </div>
    <div class="company">Volmar Capital (Asia) Ltd</div>
    <div class="brand-dot"></div>
    <div class="divider"></div>
    <div class="address">Address: 612-15 Dorrance Plaza<br>47 Faverly Street, Hong Kong</div>
    <div class="contact">
      Direct Tel # 0412 557 208<br>
      Main Tel # 0412 557 208<br>
      Fax # 0412 557 208<br>
      Email ID: info@volmar.com<br>
      Website: www.volmar.com
    </div>
  </section>

</main>
</body>
</html>
```